Need graphics designer for product packaging

We are a food service company, specializing in bringing the taste of authentic Indian sweets and savories to our customers in the US. Check out our website at www.torvilmeals.com to know more about what we do. We are looking for a graphics designer that can help design the packaging artwork for our products (gift boxes, plastic bags and bottles).

Target Market(s)

South Indian (Karnataka region)

Industry/Entity Type

Food

Colors
F0912C
F2A743
F7CA91
FBE8D2
FDF5EE
EE7325
F08F49
F5BC92
FAE3D3
FDF4ED

Requirements
Must have
• Simple, elegant, Indian style design, showcasing our logo. Please check our website for logo and colors

```html
<!DOCTYPE html>
<html lang="en">
<head>
<meta charset="utf-8">
<title>Torvil Meals – Savouries Packaging</title>
<link href="https://fonts.googleapis.com/css2?family=Lato:wght@400;700;900&display=swap" rel="stylesheet">
<style>
  :root {
    --stage: #555555;
    --saffron: #EE7325;
    --saffron-mid: #F08F49;
    --saffron-soft: #F5BC92;
    --foil-light: #FBFAF7;
    --foil-mid: #EEEBE4;
    --gold-soft: #EBDDB8;
    --gold-pale: #F4EBD3;
    --maroon: #8E2A1A;
    --white: #FFFFFF;
  }
  * { box-sizing: border-box; margin: 0; padding: 0; }
  html, body { width: 849px; height: 1200px; overflow: hidden; }
  body {
    background: var(--stage);
    font-family: "Lato", sans-serif;
    position: relative;
  }

  /* ---------- Pouch ---------- */
  .pouch {
    position: absolute;
    top: 183px;
    width: 265px;
    height: 418px;
    overflow: hidden;
    border-radius: 3px;
  }
  .pouch--classic { left: 162px; }
  .pouch--saffron { left: 451px; }

  .pouch__pattern {
    position: absolute; inset: 0;
    background: linear-gradient(160deg, var(--gold-pale) 0%, var(--foil-light) 35%, var(--gold-soft) 60%, var(--foil-light) 80%, var(--gold-pale) 100%);
  }
  .pouch__zip {
    position: absolute; left: 8px; right: 8px; top: 42px;
    height: 4px;
    border-top: 1px solid rgba(0,0,0,0.08);
    border-bottom: 1px solid rgba(0,0,0,0.08);
  }
  .pouch__lower-band {
    position: absolute; left: 0; right: 0; top: 311px; bottom: 0;
    background: linear-gradient(180deg, var(--saffron-mid), var(--saffron));
  }

  .pouch__badge {
    position: absolute; left: 50%; top: 81px;
    width: 84px; height: 84px; margin-left: -32px;
    border-radius: 50%;
    background: var(--saffron-mid);
  }
  .pouch__name {
    position: absolute; left: 20px; right: 0; top: 174px;
    text-align: center;
    font-weight: 700; font-size: 19px; line-height: 24px;
    color: var(--saffron);
  }
  .pouch__ribbon {
    position: absolute; left: 20px; right: 0; top: 214px;
    height: 19px;
    background: var(--saffron);
    color: var(--white);
    font-size: 11px; font-weight: 700;
    letter-spacing: 1.4px;
    display: flex; align-items: center; justify-content: center;
  }
  .pouch__photo {
    position: absolute; left: 20px; right: 0; top: 233px;
    height: 115px;
    background: linear-gradient(135deg, #B8742A 0%, #E3B33A 30%, #D8862F 50%, #E9CB5A 70%, #B89A45 100%);
  }
  .pouch__tagline {
    position: absolute; left: 20px; right: 0; top: 361px;
    text-align: center;
    font-weight: 700; font-size: 16px; line-height: 19px;
    color: var(--saffron);
  }
  .pouch--saffron .pouch__tagline { color: var(--white); }
  .pouch__range {
    position: absolute; left: 25px; right: 0; top: 408px;
    font-size: 6.6px; font-weight: 700; line-height: 8px;
    color: var(--saffron);
    white-space: nowrap;
  }
  .pouch--saffron .pouch__range { color: var(--white); }

  /* ---------- Gift box lid ---------- */
  .giftbox {
    position: absolute;
    left: 175px; top: 650px;
    width: 500px; height: 500px;
    border-radius: 2px;
    overflow: hidden;
    box-shadow: 0 0 0 10px var(--saffron-mid);
  }
  .giftbox__pattern {
    position: absolute; inset: 0;
    background: linear-gradient(150deg, var(--gold-pale) 0%, var(--foil-light) 30%, var(--gold-soft) 55%, var(--foil-light) 78%, var(--gold-pale) 100%);
  }
  .giftbox__brand {
    position: absolute; left: 0; right: 0; top: 150px;
    display: flex; flex-direction: column; align-items: center;
  }
  .giftbox__badge {
    width: 120px; height: 120px; border-radius: 50%;
    background: var(--saffron-mid);
  }
  .giftbox__name {
    margin-top: 24px;
    font-weight: 700; font-size: 28px;
    color: var(--saffron);
  }
  .giftbox__tagline {
    margin-top: 6px;
    font-size: 12px; font-weight: 700;
    letter-spacing: 6px;
    color: var(--maroon);
  }
</style>
</head>
<body>

  <section class="pouch pouch--classic">
    <div class="pouch__pattern" role="img" aria-label="Silver foil with an all-over gold mandala pattern"></div>
    <div class="pouch__zip"></div>
    <span class="pouch__badge"></span>
    <p class="pouch__name">TORVIL MEALS</p>
    <div class="pouch__ribbon">READY TO EAT SAVOURIES</div>
    <div class="pouch__photo" role="img" aria-label="Diamond grid of Indian savoury snacks: mixture, boondi, sev and chips"></div>
    <p class="pouch__tagline">MADE WITH LOVE ,<br>TASTES LIKE HOME</p>
    <p class="pouch__range">MASALA CASHEWS • BOMBAY MIXTURE &nbsp;• BANANA CHIPS (SPICY</p>
  </section>

  <section class="pouch pouch--saffron">
    <div class="pouch__pattern" role="img" aria-label="Silver foil with an all-over gold mandala pattern"></div>
    <div class="pouch__lower-band"></div>
    <div class="pouch__zip"></div>
    <span class="pouch__badge"></span>
    <p class="pouch__name">TORVIL MEALS</p>
    <div class="pouch__ribbon">READY TO EAT SAVOURIES</div>
    <div class="pouch__photo" role="img" aria-label="Diamond grid of Indian savoury snacks: mixture, boondi, sev and chips"></div>
    <p class="pouch__tagline">MADE WITH LOVE ,<br>TASTES LIKE HOME</p>
    <p class="pouch__range">MASALA CASHEWS • BOMBAY MIXTURE &nbsp;• BANANA CHIPS (SPICY</p>
  </section>

  <section class="giftbox">
    <div class="giftbox__pattern" role="img" aria-label="White lid with an all-over gold mandala pattern"></div>
    <div class="giftbox__brand">
      <span class="giftbox__badge"></span>
      <span class="giftbox__name">TORVIL MEALS</span>
      <span class="giftbox__tagline">BLESSINGS IN A BOX</span>
    </div>
  </section>

</body>
</html>
```